Velquor Engineering Consulting

We need a website design for a new company based in South Africa called Zendrex Consulting, it is a formidable engineering and consulting company with a background in Electrical and Mechanical design.We adopt a problem-solving methodology which allows us to present our clients with quick and flexible results. We offer complete engineering solutions from consulting, engineering design and even supply of equipment.
Target Market(s)
Government, private sector and public sector
Industry/Entity Type
Engineering Consulting
Number of Pages Required
5+ page
Colors
Designer to choose colors to be used in the design.
Requirements
Must have
- Must match the design of the profile, must enhance the profile look
Nice to have
- lates in terms of website design
Should not have
- Should be clean as the profile, should not deviate from the feel of the profile

```html
<!DOCTYPE html>
<html lang="en">
<head>
<meta charset="utf-8">
<title>Zendrex Consulting</title>
<link href="https://fonts.googleapis.com/css2?family=Raleway:wght@300;400;600;700&family=Open+Sans:wght@400;600&display=swap" rel="stylesheet">
<style>
:root{
  --ink:#2b2f36;
  --dark:#33373f;
  --darker:#24272d;
  --card:#40444c;
  --line:#6d727a;
  --text:#555a62;
  --muted:#8a8f96;
  --light:#f4f4f4;
  --grey:#dcdcdc;
  --white:#ffffff;
  --accent:#c9302c;
}
*{box-sizing:border-box;margin:0;padding:0}
html,body{width:1200px;height:4304px;overflow:hidden;background:var(--white)}
body{font-family:"Open Sans",Arial,sans-serif;color:var(--text);font-size:15px;line-height:1.6}
section,header,footer{position:relative;width:1200px;overflow:hidden}

/* header */
.topbar{height:120px;background:var(--white);border-bottom:1px solid var(--grey)}
.topbar .contact{position:absolute;top:12px;font-size:13px;display:flex;gap:8px;align-items:center;color:var(--text)}
.topbar .phone{left:40px}
.topbar .mail{right:40px}
.nav{position:absolute;top:58px;display:flex;gap:26px;font-family:"Raleway",sans-serif;font-size:13px;text-transform:uppercase;color:var(--ink);letter-spacing:.5px}
.nav.left{left:100px}
.nav.right{right:50px}
.nav .active{border:1px solid var(--ink);padding:2px 10px;margin-top:-3px}
.brand{position:absolute;left:50%;top:22px;transform:translateX(-50%);display:flex;align-items:center;gap:10px;font-family:"Raleway",sans-serif;font-weight:600;font-size:30px;color:var(--ink);letter-spacing:2px;text-transform:uppercase}
.brand .mark{width:16px;height:16px;background:var(--ink)}

/* hero */
.hero{height:520px;background:linear-gradient(180deg,#2d3138,#1f2227)}
.hero .backdrop{position:absolute;right:0;top:0;width:760px;height:520px;background:linear-gradient(120deg,rgba(255,255,255,0) 0%,rgba(180,190,200,.18) 60%,rgba(255,255,255,.05) 100%)}
.hero h1{position:absolute;left:100px;top:160px;font-family:"Raleway",sans-serif;font-weight:700;font-size:36px;line-height:1.3;color:var(--white);text-transform:uppercase;width:560px;z-index:1}
.hero .word{position:absolute;left:90px;top:300px;font-family:"Raleway",sans-serif;font-weight:300;font-size:150px;line-height:1;color:rgba(255,255,255,.1);letter-spacing:10px}
.arrow{position:absolute;top:340px;width:30px;height:40px;background:rgba(255,255,255,.85);display:flex;align-items:center;justify-content:center}
.arrow.prev{left:0}.arrow.next{right:0}

/* section headings */
.heading{text-align:center;font-family:"Raleway",sans-serif;font-weight:300;font-size:40px;letter-spacing:1px;text-transform:uppercase;color:var(--ink)}
.heading.light{color:var(--white);font-weight:600;font-size:30px}
.heading.boxed{display:flex;justify-content:center;align-items:flex-end;gap:14px}
.heading .sq{width:14px;height:14px;border:2px solid var(--ink);margin-bottom:14px}

/* about */
.about{height:720px;background:var(--white)}
.about .heading{padding-top:100px}
.about .lead{width:880px;margin:36px auto 0;text-align:center;font-size:14px}
.pillars{display:flex;justify-content:center;gap:180px;margin-top:60px;text-align:center}
.pillar{width:300px}
.pillar h3{font-family:"Raleway",sans-serif;font-weight:700;font-size:20px;color:var(--ink);margin:12px 0 8px}
.pillar p{font-size:13px}

/* dark card sections */
.darkband{height:440px;background:linear-gradient(180deg,var(--dark),var(--darker))}
.darkband .heading{padding-top:66px}
.cards{display:flex;justify-content:center;gap:30px;margin-top:48px}
.card{width:300px;height:150px;background:var(--card);border:1px solid var(--line);display:flex;gap:16px;padding:18px}
.card .icon{flex:0 0 70px;height:70px;background:#d9dbdd;border-radius:2px}
.card h4{font-family:"Raleway",sans-serif;font-weight:700;font-size:14px;color:var(--white);text-transform:uppercase;line-height:1.25;margin-bottom:8px}
.card li{font-size:12px;color:#c9ccd0;list-style:none;line-height:1.5}
.card li::before{content:"• "}
.viewall{text-align:center;margin-top:34px;font-size:12px;color:var(--white);text-transform:uppercase;letter-spacing:1px}
.viewall span{border-bottom:1px solid var(--white);padding-bottom:2px}

/* engineering */
.engineering{height:480px;background:var(--white)}
.engineering .heading{position:absolute;left:90px;top:90px;text-align:left}
.engineering p{position:absolute;left:100px;top:250px;width:480px;font-size:14px}
.engineering .photo{position:absolute;left:680px;top:70px;width:440px;height:300px;background:linear-gradient(180deg,#9fb6cc 0%,#c5b48a 60%,#6b6450 100%)}

/* consulting */
.consulting{height:320px;background:var(--white)}
.consulting .heading{padding-top:70px}
.consulting p{width:860px;margin:40px auto 0;text-align:center;font-size:14px}

/* industries */
.industries{height:480px;background:var(--grey)}
.industries .heading{padding-top:60px;font-weight:600;font-size:30px}
.sectors{display:flex;justify-content:center;gap:40px;margin-top:60px}
.sector{width:230px;height:190px;display:flex;flex-direction:column;align-items:center;justify-content:center;gap:22px;font-family:"Raleway",sans-serif;font-weight:700;font-size:15px;color:var(--ink);text-transform:uppercase}
.sector.current{border:1px solid #9a9ea4;background:#d2d2d2}
.sector .glyph{width:60px;height:60px;background:var(--ink);border-radius:4px}

/* accreditation */
.accreditation{height:300px;background:var(--white)}
.accreditation .heading{padding-top:60px;font-weight:600;font-size:30px}
.badges{display:flex;justify-content:center;align-items:center;gap:30px;margin-top:50px}
.badge{width:150px;height:64px;border:1px solid var(--grey);display:flex;align-items:center;justify-content:center}
.badge i{display:block;width:90px;height:22px;background:#9ea2a8;border-radius:3px}
.chev{color:var(--muted);font-size:26px;width:30px;text-align:center}

/* footer */
.footnav{position:relative;height:60px;background:var(--darker);display:flex;align-items:center;justify-content:space-between;padding:0 100px}
.footnav ul{display:flex;gap:22px;list-style:none;font-size:12px;color:#c8cbcf;text-transform:uppercase}
.social{display:flex;gap:10px}
.social span{width:22px;height:22px;border-radius:50%;background:#7a8088}
.contactmap{position:relative;height:380px;background:linear-gradient(135deg,#e7e6e2,#d8dde0);overflow:hidden}
.contactpanel{position:absolute;left:100px;top:0;width:330px;height:380px;background:rgba(36,39,45,.92);color:var(--white);padding:28px 30px}
.contactpanel h5{font-family:"Raleway",sans-serif;font-weight:700;font-size:16px;text-transform:uppercase;margin-bottom:24px}
.contactpanel .row{display:flex;gap:12px;font-size:13px;margin-bottom:22px;line-height:1.45}
.contactpanel .row svg{flex:0 0 18px}
.maplabel{position:absolute;left:690px;top:60px;font-family:"Raleway",sans-serif;font-weight:700;font-size:26px;color:var(--ink);text-transform:uppercase}
.pin{position:absolute;left:735px;top:104px}
.copyright{height:44px;background:var(--darker);color:#a9adb2;font-size:12px;text-align:center;line-height:44px}
</style>
</head>
<body>

<header class="topbar">
  <div class="contact phone">
    <svg width="14" height="14" viewBox="0 0 24 24"><path d="M6.6 10.8a15 15 0 0 0 6.6 6.6l2.2-2.2c.3-.3.7-.4 1-.2 1.1.4 2.3.6 3.6.6.6 0 1 .4 1 1V20c0 .6-.4 1-1 1A17 17 0 0 1 3 4c0-.6.4-1 1-1h3.5c.6 0 1 .4 1 1 0 1.3.2 2.5.6 3.6.1.3 0 .7-.2 1z" fill="#2b2f36"/></svg>
    +27 (0)11 555 0142
  </div>
  <div class="contact mail">
    <svg width="14" height="12" viewBox="0 0 24 18"><rect x="1" y="1" width="22" height="16" fill="none" stroke="#2b2f36" stroke-width="2"/><path d="M1 1l11 9 11-9" fill="none" stroke="#2b2f36" stroke-width="2"/></svg>
    info@zendrex.example
  </div>
  <nav class="nav left"><span class="active">Home</span><span>About</span><span>Products &amp; Services</span></nav>
  <div class="brand"><span class="mark"></span>Zendrex</div>
  <nav class="nav right"><span>Industries We Serve</span><span>Accreditation</span><span>Contact Us</span></nav>
</header>

<section class="hero">
  <div class="backdrop" role="img" aria-label="Photograph of a cable-stayed bridge at dusk"></div>
  <div class="word">ZENDREX</div>
  <h1>We offer complete engineering solutions from consulting, engineering design and even supply of equipment.</h1>
  <div class="arrow prev"><svg width="10" height="14" viewBox="0 0 10 14"><path d="M8 1L2 7l6 6" fill="none" stroke="#333" stroke-width="2"/></svg></div>
  <div class="arrow next"><svg width="10" height="14" viewBox="0 0 10 14"><path d="M2 1l6 6-6 6" fill="none" stroke="#333" stroke-width="2"/></svg></div>
</section>

<section class="about">
  <h2 class="heading boxed"><span class="sq"></span>About Zendrex Consulting</h2>
  <p class="lead">Established in 2016, Zendrex Consulting is a formidable engineering and consulting company with a background in Electrical and Mechanical design. We adopt a problem-solving methodology which allows us to present our clients with quick and flexible results. We offer complete engineering solutions from consulting, engineering design and even supply of equipment.<br><br>With over 15 years combined experience in Engineering and Electrical Technology, we create solutions of the highest innovative standard.</p>
  <div class="pillars">
    <div class="pillar">
      <svg width="44" height="40" viewBox="0 0 44 40"><path d="M4 4h36v24H18l-8 8v-8H4z" fill="none" stroke="#2b2f36" stroke-width="3" stroke-linejoin="round"/><path d="M12 13h20M12 19h14" stroke="#2b2f36" stroke-width="3"/></svg>
      <h3>OUR VISION</h3>
      <p>We aim to become the preferred engineering design and consulting firm within the South African Engineering industry for government and private sectors.</p>
    </div>
    <div class="pillar">
      <svg width="40" height="40" viewBox="0 0 40 40"><path d="M8 38V4M8 6h24l-6 8 6 8H8" fill="none" stroke="#2b2f36" stroke-width="3" stroke-linejoin="round"/></svg>
      <h3>OUR MISSION</h3>
      <p>We offer our clients technology and innovative services, allowing us to make high levels of customer satisfaction.</p>
    </div>
  </div>
</section>

<section class="darkband">
  <h2 class="heading light">Our Products &amp; Services</h2>
  <div class="cards">
    <div class="card"><div class="icon" role="img" aria-label="Engineer icon"></div><div><h4>Electrical Engineering &amp; Installation</h4><ul><li>Project Management</li><li>Commissioning</li><li>Equipment supply and quality</li></ul></div></div>
    <div class="card"><div class="icon" role="img" aria-label="Design icon"></div><div><h4>Electrical Design</h4><ul><li>We offer our complete load and equipment design to suit your building</li></ul></div></div>
    <div class="card"><div class="icon" role="img" aria-label="Electrification icon"></div><div><h4>Turnkey Electrification</h4><ul><li>Complete turnkey services from start to finish for your development</li></ul></div></div>
  </div>
  <div class="viewall"><span>View all +</span></div>
</section>

<section class="engineering">
  <h2 class="heading boxed"><span class="sq"></span>Zendrex Engineering</h2>
  <p>Using innovation and technology, we provide a range of Mechanical and Electrical design, electrification, equipment supply, mechanical and electrical products to mining houses, process plants, government departments, municipalities, state owned entities and companies.</p>
  <div class="photo" role="img" aria-label="Photograph of construction cranes and engineers on a building site"></div>
</section>

<section class="darkband">
  <h2 class="heading light">Our Services</h2>
  <div class="cards">
    <div class="card"><div class="icon" role="img" aria-label="Review icon"></div><div><h4>Engineering Design Reviews</h4><ul><li>Design Validation</li><li>Equipment Sizing</li><li>Practicality Assessment</li></ul></div></div>
    <div class="card"><div class="icon" role="img" aria-label="Advice icon"></div><div><h4>Technical Advice</h4><ul><li>Writing Best Codes of practice</li><li>Equipment trade-off</li><li>Feasibility Assessment</li></ul></div></div>
    <div class="card"><div class="icon" role="img" aria-label="Execution icon"></div><div><h4>Our Execution</h4><ul><li>Project Completion Reports</li><li>Supervision</li><li>Operational Assistance</li></ul></div></div>
  </div>
</section>

<section class="consulting">
  <h2 class="heading boxed"><span class="sq"></span>Zendrex Consulting</h2>
  <p>Our consulting arm is focused on developing high level technical training and consulting solutions for our clients. We take a detailed solutions approach to engineering projects in various industries including mining, transport and construction among others.</p>
</section>

<section class="industries">
  <h2 class="heading">Industries We Serve</h2>
  <div class="sectors">
    <div class="sector"><span class="glyph" role="img" aria-label="Mining icon"></span>Mining</div>
    <div class="sector current"><span class="glyph" role="img" aria-label="Construction icon"></span>Construction</div>
    <div class="sector"><span class="glyph" role="img" aria-label="Public sector icon"></span>Public Sector</div>
    <div class="sector"><span class="glyph" role="img" aria-label="EPCM icon"></span>EPCMs</div>
  </div>
</section>

<section class="accreditation">
  <h2 class="heading">Accreditation Bodies</h2>
  <div class="badges">
    <span class="chev">‹</span>
    <div class="badge"><i></i></div><div class="badge"><i></i></div><div class="badge"><i></i></div><div class="badge"><i></i></div><div class="badge"><i></i></div>
    <span class="chev">›</span>
  </div>
</section>

<footer>
  <div class="footnav">
    <ul><li>Home</li><li>About</li><li>Products &amp; Services</li><li>Industries We Serve</li><li>Accreditation</li><li>Contact Us</li></ul>
    <div class="social"><span></span><span></span><span></span><span></span><span></span><span></span></div>
  </div>
  <div class="contactmap" role="img" aria-label="Street map showing the office location">
    <div class="contactpanel">
      <h5>Contact Details</h5>
      <div class="row"><svg width="18" height="20" viewBox="0 0 24 24"><path d="M12 2a7 7 0 0 0-7 7c0 5 7 13 7 13s7-8 7-13a7 7 0 0 0-7-7z" fill="#fff"/></svg><span>Zendrex Consulting<br>12 Ridgeview Lane, Greenhill,<br>Midrand, 1685, South Africa</span></div>
      <div class="row"><svg width="18" height="18" viewBox="0 0 24 24"><path d="M6.6 10.8a15 15 0 0 0 6.6 6.6l2.2-2.2c.3-.3.7-.4 1-.2 1.1.4 2.3.6 3.6.6.6 0 1 .4 1 1V20c0 .6-.4 1-1 1A17 17 0 0 1 3 4c0-.6.4-1 1-1h3.5c.6 0 1 .4 1 1 0 1.3.2 2.5.6 3.6.1.3 0 .7-.2 1z" fill="#fff"/></svg><span>+27 (0)11 555 0142</span></div>
      <div class="row"><svg width="18" height="14" viewBox="0 0 24 18"><rect x="1" y="1" width="22" height="16" fill="none" stroke="#fff" stroke-width="2"/><path d="M1 1l11 9 11-9" fill="none" stroke="#fff" stroke-width="2"/></svg><span>info@zendrex.example</span></div>
    </div>
    <div class="maplabel">Zendrex</div>
    <svg class="pin" width="30" height="40" viewBox="0 0 24 32"><path d="M12 1a10 10 0 0 0-10 10c0 8 10 20 10 20s10-12 10-20A10 10 0 0 0 12 1z" fill="#24272d"/><circle cx="12" cy="11" r="4" fill="#c9302c"/></svg>
  </div>
  <div class="copyright">Copyright © 2019 Zendrex Consulting. All Rights Reserved</div>
</footer>

</body>
</html>
```